Website Design for new business Brightfield Junior Games

We need a website for our new business Brightfield Junior Games which is about teaching kids from 5 years to 16 years of age how to play either Australian Rules Football or Soccer. Need area for Soccer and Football plus Coaches section, and schedule for each training etc. NEW LOGO ADDED

Target Market(s)

Adults with kids from 5 to 16 looking for specialist coaches to train their kids

Industry/Entity Type

Fitness

Number of Pages Required

5+ page

Colors
3176b5
ffc214

Requirements
Must have
• Logo
• How, Why and What
Nice to have
• I like this website http://www.tallyhoopers.com.au/
• http://www.meadowkickdrills.com.au/ is another site that is okay
Should not have
• Our competitor is this website http://www.pitchcometschooling.com.au/ but I don't like their website style not kid or parent friendly

```html
<!DOCTYPE html>
<html lang="en">
<head>
<meta charset="utf-8">
<title>Brightfield Junior Games</title>
<link rel="stylesheet" href="https://fonts.googleapis.com/css2?family=Ubuntu:wght@400;500;700&family=Play:wght@400;700&display=swap">
<style>
:root{
  --navy:#262b6e;
  --navy-deep:#1d2159;
  --yellow:#fdc314;
  --orange:#f39c12;
  --nav-green:#0e6a2b;
  --btn-green:#1fb956;
  --btn-text:#0b4d24;
  --grass-a:#4f8a23;
  --grass-b:#2f6515;
  --bar:#1b1b1b;
  --footer:#2a2a2a;
  --light:#f2f2f2;
  --white:#ffffff;
}
*{box-sizing:border-box;margin:0;padding:0}
html,body{width:1200px;height:2590px;overflow:hidden;background:var(--white)}
body{position:relative;font-family:"Play",sans-serif;color:var(--white)}
.abs{position:absolute}
a{color:inherit;text-decoration:none}

.topbar{left:0;top:0;width:1200px;height:28px;background:var(--bar);font-size:12px;line-height:28px}
.topbar .links{left:120px}
.topbar .links span{margin-right:24px}
.topbar .countdown{right:110px}
.topbar b{margin-right:12px}

.header{left:0;top:28px;width:1200px;height:92px;background:var(--navy)}
.brand{top:24px;display:flex;align-items:center;gap:6px;font-family:"Ubuntu",sans-serif;font-weight:700;font-size:13px;color:var(--white);width:120px;line-height:1.1}
.brand i{flex:0 0 22px;height:22px;border-radius:50%;background:var(--white)}
.brand.left{left:88px}
.brand.right{left:1030px}
.tagline{left:0;width:1200px;top:20px;text-align:center;font-family:"Ubuntu",sans-serif;font-weight:500;font-size:38px;color:var(--yellow)}

.mainnav{left:0;top:120px;width:1200px;height:23px;background:var(--nav-green);font-family:"Ubuntu",sans-serif;font-weight:700;font-size:14px;line-height:23px}
.mainnav ul{position:absolute;right:92px;display:flex;gap:40px;list-style:none}

.hero{left:0;top:143px;width:1200px;height:531px;background:linear-gradient(180deg,#8e9f8a 0%,#a6b69a 45%,#6f9a4e 75%,#4d7d2c 100%)}
.hero-title{left:0;width:1200px;top:88px;text-align:center;font-family:"Ubuntu",sans-serif;font-weight:500;font-size:46px;line-height:62px;color:var(--navy-deep)}
.hero-sub{left:0;width:1200px;top:241px;text-align:center;font-family:"Ubuntu",sans-serif;font-weight:700;font-size:21px;line-height:28px;color:var(--navy-deep)}
.hero-sub a{text-decoration:underline}
.trial{left:368px;top:354px;width:445px;height:57px;border-radius:6px;background:var(--btn-green);color:var(--btn-text);font-family:"Ubuntu",sans-serif;font-weight:700;font-size:36px;line-height:57px;text-align:center}

.grass{left:0;width:1200px;background:linear-gradient(180deg,var(--grass-a),var(--grass-b) 50%,var(--grass-a))}
.info{top:674px;height:276px}
.card{top:25px;width:316px;height:220px;border-radius:10px;background:var(--yellow);color:var(--white);padding:10px 14px}
.card.dark{background:var(--navy)}
.card h2{font-family:"Ubuntu",sans-serif;font-weight:500;font-size:24px;text-align:center;color:var(--navy-deep);margin-bottom:10px}
.card.dark h2{color:var(--yellow)}
.card p{font-size:13px;line-height:18px}
.card .more{position:absolute;right:14px;bottom:12px;font-size:11px;color:var(--navy-deep)}
.card.dark .more{color:var(--yellow)}

.section-title{left:0;width:1200px;text-align:center;font-family:"Ubuntu",sans-serif;font-size:22px;color:var(--white)}
.divider{left:442px;width:316px;height:16px}

.coaches{left:0;top:950px;width:1200px;height:449px;background:linear-gradient(180deg,#1e2a44 0%,#2f405e 45%,#3d5a3a 78%,#1f4a1a 100%)}
.coach-panel{left:130px;top:138px;width:958px;height:190px;background:rgba(30,40,70,.65)}
.coach-photo{left:0;top:0;width:181px;height:190px;background:linear-gradient(180deg,#c9ccd4,#5a6a8a)}
.coach-text{left:206px;top:10px;width:735px;font-size:12.5px;line-height:15px}
.coach-text h3{font-family:"Ubuntu",sans-serif;font-size:14px;font-weight:500}
.coach-text .role{color:var(--yellow);font-size:14px;margin-bottom:6px}
.coach-text p{margin-bottom:10px}
.dots{top:417px;left:458px;display:flex;gap:10px}
.dots i{width:86px;height:3px;background:rgba(255,255,255,.45)}
.dots i:first-child{background:var(--white)}

.blog{top:1399px;height:535px}
.post{top:117px;width:316px;height:366px;background:rgba(20,50,10,.72);border-radius:4px;overflow:hidden}
.post .thumb{height:180px}
.post h3{font-family:"Ubuntu",sans-serif;font-weight:700;font-size:14px;line-height:16px;color:var(--yellow);padding:18px 16px 14px}
.post p{font-size:11px;line-height:12.5px;padding:0 16px}
.post .date{position:absolute;left:16px;bottom:10px;font-size:10px;color:#c8d2bf}

.team{left:0;top:1934px;width:1200px;height:349px;background:var(--light)}
.team-title{left:0;width:1200px;top:20px;text-align:center;font-family:"Ubuntu",sans-serif;font-weight:700;font-size:22px;color:var(--orange)}
.team-title span{color:var(--navy)}
.avatars{left:108px;width:984px;display:flex;justify-content:space-between}
.avatars i{width:69px;height:69px;border-radius:50%}
.pager{left:570px;top:324px;width:44px;height:20px;background:#c8c8c8;color:var(--white);font-size:11px;line-height:20px;text-align:center}

.newsletter{top:2283px;height:230px}
.subscribe{left:181px;top:78px;width:831px;height:53px;border:1px solid rgba(255,255,255,.6);border-radius:3px;background:rgba(120,170,80,.25)}
.subscribe span{position:absolute;right:0;top:0;width:171px;height:51px;background:var(--navy-deep);text-align:center;line-height:51px;font-size:14px}
.follow{left:490px;top:175px;display:flex;align-items:center;gap:10px;font-size:11px;font-weight:700}
.follow i{width:28px;height:28px;border-radius:50%;border:1.5px solid var(--white)}
.follow b{margin-right:14px}

.footer{left:0;top:2513px;width:1200px;height:77px;background:var(--footer)}
.footer h4{position:absolute;left:100px;top:12px;font-family:"Ubuntu",sans-serif;font-weight:500;font-size:17px}
.footer .company{position:absolute;left:100px;top:48px;font-size:12px;display:flex;align-items:center;gap:6px}
.footer .company i{width:14px;height:14px;border-radius:50%;background:#666}
.footer .year{position:absolute;left:1056px;top:30px;font-size:13px;font-weight:700}
</style>
</head>
<body>

<div class="abs topbar">
  <div class="abs links"><span>Home</span><span>Pages</span><span>Typography</span></div>
  <div class="abs countdown"><b>Next Game:</b>182 days &nbsp;15 hrs &nbsp;35 min &nbsp;41 sec</div>
</div>

<header class="abs header">
  <div class="abs brand left"><i></i>Brightfield Junior Games</div>
  <h1 class="abs tagline">Where Kids are Champions</h1>
  <div class="abs brand right"><i></i>Brightfield Junior Games</div>
</header>

<nav class="abs mainnav">
  <ul><li>Home Pages</li><li>Feature Pages</li><li>Mega Menu ⌄</li><li>Header Variations</li><li>Blog Options</li></ul>
</nav>

<section class="abs hero" role="img" aria-label="Young children in training bibs playing soccer on a grass pitch with a goal behind">
  <h2 class="abs hero-title">Specialist sports coaching<br>for boys &amp; girls 5 to 16 years old</h2>
  <p class="abs hero-sub">Is your child the next champion?<br><a href="#">Click here for details</a></p>
  <a class="abs trial" href="#">TWO WEEK FREE TRIAL</a>
</section>

<section class="abs grass info" role="img" aria-label="Close-up grass field background">
  <article class="abs card" style="left:98px">
    <h2>Why we do it</h2>
    <p>We are all about getting kids away from computer games and to start living life in a healthy and productive way. We aim to teach the kids how to play their chosen sport, have lots of FUN and help with their personal development for life's challenges. So whether your child wants to become a weekend warrior or just learn ...</p>
    <span class="more">Read More</span>
  </article>
  <article class="abs card dark" style="left:442px">
    <h2>How we do it</h2>
    <p>We start teaching boys &amp; girls from 5 years old basic skills of how to play their chosen sport. We introduce aspects of nutrition, fitness, physical preparation, injury prevention and other advanced concepts as your child progresses up until 16 years of age.</p>
    <span class="more">Read More</span>
  </article>
  <article class="abs card" style="left:786px">
    <h2>What we do</h2>
    <p>We hold weekly sessions for kids from 5 to 8, 9 to 12 and 12 to 16 years of age. We also have 3 day holiday programs and for those children that have talent and want to explore their chosen sport further we have elite squads.</p>
    <span class="more">Read More</span>
  </article>
</section>

<section class="abs coaches" role="img" aria-label="Floodlit stadium with a large football on the pitch">
  <h2 class="abs section-title" style="top:40px">Coaches – Australian Rules</h2>
  <svg class="abs divider" style="top:83px" viewBox="0 0 316 16"><line x1="0" y1="8" x2="316" y2="8" stroke="#fdc314" stroke-width="1"/><circle cx="158" cy="8" r="8" fill="#2d3a8c" stroke="#fff" stroke-width="1"/></svg>
  <div class="abs coach-panel">
    <div class="abs coach-photo" role="img" aria-label="Portrait of coach Daniel Whitmore in front of a sponsor board"></div>
    <div class="abs coach-text">
      <h3>About Daniel Whitmore</h3>
      <div class="role">-Owen Pritchard</div>
      <p>Daniel Whitmore played over 200 games of football for Ridgeway, Larkford &amp; Seabrook over his decade of playing the game. He is one who loves the game and wants to teach others how to play and have fun.</p>
      <p>In 2006 he reached out into coaching and over the past 10 years he has achieved arguably the best coaching record in local football including 4 senior premierships with Elmstead Wallabies, Parkvale and Harbour City. He has also coached junior teams and knows the difference between young kids playing the game for fun and professional weekend warriors.</p>
      <p>Let Daniel teach your child not just how to play Australian Rules football but also how to develop as a person into a more rounded and self confident person for the journey ahead of them.</p>
    </div>
  </div>
  <div class="abs dots"><i></i><i></i><i></i></div>
</section>

<section class="abs grass blog" role="img" aria-label="Grass field background">
  <h2 class="abs section-title" style="top:22px">From our Blog</h2>
  <svg class="abs divider" style="top:64px" viewBox="0 0 316 16"><line x1="0" y1="8" x2="316" y2="8" stroke="#ffffff" stroke-width="1"/><circle cx="158" cy="8" r="8" fill="#2d3a8c" stroke="#fff" stroke-width="1"/></svg>
  <article class="abs post" style="left:98px">
    <div class="thumb" role="img" aria-label="Two young soccer players holding balls on a field" style="background:linear-gradient(180deg,#b9d3ec,#e6eef5 60%,#7fa04c)"></div>
    <h3>Curabitur mattis tellus rutrum enim facilisis</h3>
    <p>Lorem Ipsum is simply dummy text of the printing and typesetting industry. Lorem Ipsum is simply dummy text of the printing and typesetting industry. Lorem Ipsum has been the industry's standard dummy text ever since the 1500s, Lorem Ipsum has been the industry's standard dummy text ever since the 1500s.</p>
    <span class="date">Written on Thursday , 28 Jan 2016, 08:54pm</span>
  </article>
  <article class="abs post" style="left:442px">
    <div class="thumb" role="img" aria-label="Two worn soccer balls resting on grass" style="background:linear-gradient(180deg,#1f7a44,#2e8d4f 55%,#176b34)"></div>
    <h3>Curabitur mattis tellus rutrum enim facilisis</h3>
    <p>Lorem Ipsum is simply dummy text of the printing and typesetting industry. Lorem Ipsum is simply dummy text of the printing and typesetting industry. Lorem Ipsum has been the industry's standard dummy text ever since the 1500s, Lorem Ipsum has been the industry's standard dummy text ever since the 1500s.</p>
    <span class="date">Written on Thursday , 28 Jan 2016, 08:54pm</span>
  </article>
  <article class="abs post" style="left:786px">
    <div class="thumb" role="img" aria-label="Three smiling children holding sports balls" style="background:linear-gradient(180deg,#6fb04a,#d9a080 50%,#c24a5a)"></div>
    <h3>Curabitur mattis tellus rutrum enim facilisis</h3>
    <p>Lorem Ipsum is simply dummy text of the printing and typesetting industry. Lorem Ipsum is simply dummy text of the printing and typesetting industry. Lorem Ipsum has been the industry's standard dummy text ever since the 1500s, Lorem Ipsum has been the industry's standard dummy text ever since the 1500s.</p>
    <span class="date">Written on Thursday , 28 Jan 2016, 08:54pm</span>
  </article>
</section>

<section class="abs team">
  <h2 class="abs team-title">Over 200 members and growing,<span>We love our team.</span></h2>
  <svg class="abs divider" style="top:55px" viewBox="0 0 316 16"><line x1="0" y1="8" x2="316" y2="8" stroke="#fdc314" stroke-width="1"/><circle cx="158" cy="8" r="8" fill="#2d3a8c" stroke="#fff" stroke-width="1"/></svg>
  <div class="abs avatars" style="top:126px" role="img" aria-label="Round member photos of young players">
    <i style="background:#c9b8a6"></i><i style="background:#5f8b46"></i><i style="background:#b2323f"></i><i style="background:#8b6a4d"></i><i style="background:#6a8a3a"></i><i style="background:#6a8fc0"></i><i style="background:#b03a44"></i><i style="background:#cfc9c2"></i><i style="background:#8c7a64"></i><i style="background:#4f7fb8"></i><i style="background:#8fbf6a"></i><i style="background:#a9a39b"></i>
  </div>
  <div class="abs avatars" style="top:229px" role="img" aria-label="Round member photos of young players">
    <i style="background:#7a6a50"></i><i style="background:#9bb678"></i><i style="background:#c8a97d"></i><i style="background:#b2323f"></i><i style="background:#cfc9c2"></i><i style="background:#a57860"></i><i style="background:#4f7fb8"></i><i style="background:#8fbf6a"></i><i style="background:#a9a39b"></i><i style="background:#5f8b46"></i><i style="background:#b03a44"></i><i style="background:#7a6a50"></i>
  </div>
  <div class="abs pager">‹ ›</div>
</section>

<section class="abs grass newsletter" role="img" aria-label="Grass field background">
  <h2 class="abs section-title" style="top:22px">Sign up for our newsletter</h2>
  <div class="abs subscribe"><span>Subscribe</span></div>
  <div class="abs follow"><b>Follow</b><i></i><i></i><i></i><i></i></div>
</section>

<footer class="abs footer">
  <h4>Have a question or comment</h4>
  <div class="company"><i></i>Brightfield Junior Games Pty Ltd</div>
  <div class="year">2016</div>
</footer>

</body>
</html>
```